Real Estate Postcard Design

I need a personal postcard designed. I have gone on my MAC and laid out a postcard. I am not a designer so feel free to move things around. If you can use my exact text that would be great. The photos are sample photos so you will need me to tell you what size and resolution you need me to send my sold photos. I have a total of 46 sold properties and 5 Listings.
Feel free to size boxes accordingly. I will send over my office logo info as well as the logos.
Please feel free to call me if need be.
Thank you.
Marla Trevin
614-392-8807

Industry/Entity Type

Real Estate

```html
<!DOCTYPE html>
<html lang="en">
<head>
<meta charset="utf-8">
<title>More Sold's By Marla – Postcard Inside</title>
<link rel="stylesheet" href="https://fonts.googleapis.com/css2?family=Rosario:wght@700&family=Roboto+Condensed:wght@400;700&family=Arimo&display=swap">
<style>
  :root{
    --green:#1e6b3b;
    --green-dark:#17592f;
    --fold:#14472a;
    --yellow:#f4e71c;
    --white:#ffffff;
    --ink:#111111;
    --red:#e0262b;
  }
  *{box-sizing:border-box;margin:0;padding:0}
  html,body{width:950px;height:1200px;overflow:hidden;background:var(--white)}
  body{position:relative;font-family:"Roboto Condensed",Arial,sans-serif}

  .side-label{position:absolute;color:#333;font-family:"Arimo",Arial,sans-serif;font-size:17px}
  .inside-label{top:18px;left:0;width:950px;text-align:center}
  .fold-label{left:-22px;top:565px;transform:rotate(-90deg);font-size:18px}
  .fold-marker{position:absolute;top:587px}
  .fold-marker.left{left:38px}
  .fold-marker.right{left:900px}

  .panel{position:absolute;left:50px;top:50px;width:850px;height:1075px;background:var(--green)}
  .title-band{height:54px;background:var(--green-dark);border-bottom:2px solid var(--white);
    display:flex;align-items:center;justify-content:center}
  .title-band h1{font-family:"Rosario","Optima",sans-serif;font-weight:700;font-size:31px;color:var(--white);letter-spacing:.3px}

  .sold-grid{position:absolute;left:6px;right:6px;display:grid;
    grid-template-columns:repeat(4,minmax(0,1fr));grid-template-rows:repeat(4,114px);gap:3px 3px}
  .sold-grid.upper{top:62px}
  .sold-grid.lower{top:563px}

  .fold-line{position:absolute;left:0;right:0;top:544px;height:2px;background:var(--fold)}

  .tile{display:flex;flex-direction:column;min-width:0}
  .photo{flex:1;background:linear-gradient(180deg,#b9cfe2 0%,#b9c1bd 50%,#6e9446 100%)}
  .photo.grey{background:linear-gradient(180deg,#c3ced6 0%,#9a9c98 55%,#6c8d45 100%)}
  .photo.white{background:linear-gradient(180deg,#9dbfe3 0%,#e6e9ea 50%,#79a04a 100%)}
  .photo.wooded{background:linear-gradient(180deg,#7c9466 0%,#7d8076 55%,#4f7a31 100%)}
  .photo.water{background:linear-gradient(180deg,#b6d0ea 0%,#86a7bf 55%,#4a6e8c 100%)}
  .photo.winter{background:linear-gradient(180deg,#9ebfe4 0%,#b9bdbf 50%,#eef2f5 100%)}

  .caption{height:20px;display:flex;align-items:center;justify-content:space-between;gap:4px;background:var(--green)}
  .addr{color:var(--white);font-weight:700;font-size:10px;padding-left:6px;white-space:nowrap;overflow:hidden;min-width:0}
  .price{flex:none;height:20px;background:var(--yellow);color:var(--ink);font-weight:700;font-size:10px;
    display:flex;align-items:center;padding:0 5px 0 11px;white-space:nowrap;
    clip-path:polygon(8px 0,100% 0,100% 100%,8px 100%,0 50%)}

  .contact-band{position:absolute;left:0;right:0;bottom:0;height:47px;display:flex;align-items:center;justify-content:center;
    font-family:"Rosario","Optima",sans-serif;font-weight:700;font-size:17.5px;color:var(--white);gap:10px}
  .contact-band .agent{color:var(--yellow)}
  .contact-band .sep{font-weight:400;opacity:.9}
</style>
</head>
<body>
  <div class="side-label inside-label">inside</div>
  <div class="side-label fold-label">Center fold</div>
  <svg class="fold-marker left" width="12" height="16" viewBox="0 0 12 16"><polygon points="0,0 12,8 0,16" fill="#e0262b"/></svg>
  <svg class="fold-marker right" width="12" height="16" viewBox="0 0 12 16"><polygon points="12,0 0,8 12,16" fill="#e0262b"/></svg>

  <main class="panel">
    <header class="title-band"><h1>More Sold’s By Marla</h1></header>

    <section class="sold-grid upper">
      <article class="tile"><div class="photo grey" role="img" aria-label="Photo of sold home with deck"></div><div class="caption"><span class="addr">512 Harwood Road, Chatham</span><span class="price">$310,000</span></div></article>
      <article class="tile"><div class="photo white" role="img" aria-label="Photo of sold white colonial home"></div><div class="caption"><span class="addr">14 Salt Village Lane, Chatham</span><span class="price">$765,000</span></div></article>
      <article class="tile"><div class="photo grey" role="img" aria-label="Photo of sold shingled home"></div><div class="caption"><span class="addr">6 Bayberry Road, Chatham</span><span class="price">$873,500</span></div></article>
      <article class="tile"><div class="photo winter" role="img" aria-label="Photo of sold home in snow"></div><div class="caption"><span class="addr">318 Heron Cove Road, Orleans</span><span class="price">$925,000</span></div></article>

      <article class="tile"><div class="photo" role="img" aria-label="Photo of sold blue cape with garage"></div><div class="caption"><span class="addr">24 Dune Lane, Chatham</span><span class="price">$950,000</span></div></article>
      <article class="tile"><div class="photo" role="img" aria-label="Photo of sold yellow colonial home"></div><div class="caption"><span class="addr">36 Elmwood Lane, Cotuit</span><span class="price">$255,000</span></div></article>
      <article class="tile"><div class="photo wooded" role="img" aria-label="Photo of sold cape among trees"></div><div class="caption"><span class="addr">8 Alden Lane, Eastham</span><span class="price">$405,000</span></div></article>
      <article class="tile"><div class="photo white" role="img" aria-label="Photo of sold white home with fence"></div><div class="caption"><span class="addr">17 Saltmeadow Lane, Chatham</span><span class="price">$665,000</span></div></article>

      <article class="tile"><div class="photo wooded" role="img" aria-label="Photo of sold property with lawn and trees"></div><div class="caption"><span class="addr">384 Birch Street, Chatham</span><span class="price">$670,000</span></div></article>
      <article class="tile"><div class="photo" role="img" aria-label="Photo of sold ranch home with garden"></div><div class="caption"><span class="addr">42 Kettle Road, Chatham</span><span class="price">$425,000</span></div></article>
      <article class="tile"><div class="photo grey" role="img" aria-label="Photo of sold large shingled home"></div><div class="caption"><span class="addr">41 Church Street, Chatham</span><span class="price">$1,854,000</span></div></article>
      <article class="tile"><div class="photo wooded" role="img" aria-label="Photo of sold cape with chimney"></div><div class="caption"><span class="addr">126 Gull Island Road, Chatham</span><span class="price">$2,250,000</span></div></article>

      <article class="tile"><div class="photo" role="img" aria-label="Photo of sold shingled home on lawn"></div><div class="caption"><span class="addr">83 Beacon Hill, Chatham</span><span class="price">$1,375,000.00</span></div></article>
      <article class="tile"><div class="photo" role="img" aria-label="Photo of sold home with stone steps"></div><div class="caption"><span class="addr">451 Oyster Harbor Road, Chatham</span><span class="price">$2,800,000</span></div></article>
      <article class="tile"><div class="photo water" role="img" aria-label="Photo of waterfront dock view"></div><div class="caption"><span class="addr">12 Marsh View, Chatham</span><span class="price">$472,500</span></div></article>
      <article class="tile"><div class="photo wooded" role="img" aria-label="Photo of sold grey cape in woods"></div><div class="caption"><span class="addr">37 Beachplum Lane, Chatham</span><span class="price">$550,000</span></div></article>
    </section>

    <div class="fold-line"></div>

    <section class="sold-grid lower">
      <article class="tile"><div class="photo grey" role="img" aria-label="Photo of sold cottage with patio"></div><div class="caption"><span class="addr">348A County Highway, Eastham</span><span class="price">$382,500</span></div></article>
      <article class="tile"><div class="photo grey" role="img" aria-label="Photo of sold shingled home with portico"></div><div class="caption"><span class="addr">352 Mill Street, Chatham</span><span class="price">$1,029,500</span></div></article>
      <article class="tile"><div class="photo" role="img" aria-label="Photo of sold ranch home on lawn"></div><div class="caption"><span class="addr">209 Tern Drive, Chatham</span><span class="price">$327,500</span></div></article>
      <article class="tile"><div class="photo white" role="img" aria-label="Photo of sold long shingled home"></div><div class="caption"><span class="addr">4 Tide Way, Harwich</span><span class="price">$3,700,000</span></div></article>

      <article class="tile"><div class="photo" role="img" aria-label="Photo of sold home with hydrangeas"></div><div class="caption"><span class="addr">52 Pond Lane, Chatham</span><span class="price">$575,000</span></div></article>
      <article class="tile"><div class="photo white" role="img" aria-label="Photo of sold home with porch"></div><div class="caption"><span class="addr">117 Birch Street, Chatham</span><span class="price">$777,250</span></div></article>
      <article class="tile"><div class="photo grey" role="img" aria-label="Photo of sold shingled home with red door"></div><div class="caption"><span class="addr">16 Pilgrim Road, Chatham</span><span class="price">$1,750,000</span></div></article>
      <article class="tile"><div class="photo wooded" role="img" aria-label="Photo of sold cape under trees"></div><div class="caption"><span class="addr">452 Ridge Road, Chatham</span><span class="price">$397,500</span></div></article>

      <article class="tile"><div class="photo" role="img" aria-label="Photo of sold cape with garden"></div><div class="caption"><span class="addr">618 Harwood Road, Chatham</span><span class="price">$349,000</span></div></article>
      <article class="tile"><div class="photo wooded" role="img" aria-label="Photo of sold ranch with driveway"></div><div class="caption"><span class="addr">34 Quail Lane, Dennis</span><span class="price">$450,000</span></div></article>
      <article class="tile"><div class="photo" role="img" aria-label="Photo of sold cape with green shutters"></div><div class="caption"><span class="addr">27 Clam Cove Road, Chatham</span><span class="price">$265,000</span></div></article>
      <article class="tile"><div class="photo" role="img" aria-label="Photo of sold cape with picket fence"></div><div class="caption"><span class="addr">31 Sandy Neck Road, Chatham</span><span class="price">$1,050,000</span></div></article>

      <article class="tile"><div class="photo white" role="img" aria-label="Photo of sold home with garage"></div><div class="caption"><span class="addr">58 Holly Lane, Chatham</span><span class="price">$639,000</span></div></article>
      <article class="tile"><div class="photo grey" role="img" aria-label="Photo of sold shingled home with dormer"></div><div class="caption"><span class="addr">6 Sea Spray, Harwich</span><span class="price">$1,060,000</span></div></article>
      <article class="tile"><div class="photo grey" role="img" aria-label="Photo of sold cape with garage"></div><div class="caption"><span class="addr">284 Maple Street, Chatham</span><span class="price">$715,000</span></div></article>
      <article class="tile"><div class="photo wooded" role="img" aria-label="Photo of sold home behind trees"></div><div class="caption"><span class="addr">3 Bradford Drive, Orleans</span><span class="price">$625,000</span></div></article>
    </section>

    <footer class="contact-band">
      <span class="agent">Marla Ann Trevin</span><span class="sep">|</span>
      <span>Marla@CedarDuneRealty.com</span><span class="sep">|</span>
      <span>MarlaAnnTrevin.com</span><span class="sep">|</span>
      <span>614 392-8807</span>
    </footer>
  </main>
</body>
</html>
```